Wordpress Design Project for Employee Communications Site

We need a Wordpress design for a company that strategizes on and produces materials for employee communications. Improving employee communications at all levels of an organization can help improve overall company performance and results. The site needs to look very clean and professional; we're not afraid of white space. We like the functionality that Wordpress provides; however, we only want one "true" blog page; the other pages should give the impression of a more "static" web site - particularly the home page. I have a logo that I can provide.

I have added these comments to the discussion page:
Great question - thank you for asking it. I’ve done more research

I like the very clean and monochromatic looks to many of these. I don’t have to have monochromatic, but I do like minimal colors. Simple, clean, organized. The home page should “fit” almost entirely without scrolling. I do like fat footers that you can scroll down to. I don’t want a colored background, but any that I’ve chosen with colored backgrounds could be switched to a white background.

http://www.moravelkinst.com/
http://pondrix.com/
http://v1.belmarquist.com/
http://howtheotter.com/
http://stayingnimble.com/
http://www.interiors.pelmun.co.uk/
http://brixalumnihub.com/

These last two are more corporate sites. The first one is from a well-respected consultant in my area who does a lot of what I do. And I think Harwick does a nice job with their site. So, I want to marry the look I like with getting the content job done.

http://www.messagefuelworks.com/
http://www.harwick.com/view/en_US/us/index.htm

Target Market(s)

Target market is mid- to large-sized companies. More than 500 employees.

Industry/Entity Type

Communications

Requirements
Must have
• Need an impactful home page. There should be a "blog" page; contact us; services; about. For starters, at least. I want fonts to be very readable - that is, either quite dark gray or black.
Nice to have
• I am loathe to include a picture of myself, but I do want some images that say, "professional" and "expert" in communications.
Should not have
• I don't want a hits counter :) (I know no one would do that!).

```html
<!DOCTYPE html>
<html lang="en">
<head>
<meta charset="utf-8">
<title>Workforce Messaging Group</title>
<link rel="stylesheet" href="https://fonts.googleapis.com/css2?family=Encode+Sans+Condensed:wght@400;500;600&family=Open+Sans:wght@400;700&family=PT+Sans:wght@400;700&display=swap">
<style>
:root{
  --lime:#c4dc3c;
  --lime-soft:#d8ea8e;
  --sky:#8fd3f3;
  --sky-deep:#5cbbe8;
  --footer-sky:#addff4;
  --ink:#333333;
  --ink-soft:#3d3d3d;
  --rule:#dcdcdc;
  --brand:#5a4f7d;
}
*{margin:0;padding:0;box-sizing:border-box}
html,body{width:1200px;height:1052px;overflow:hidden}
body{position:relative;background:#fff;font-family:"PT Sans",Tahoma,sans-serif;color:var(--ink)}
.top-band{position:absolute;left:0;top:0;width:1200px;height:10px;background:var(--lime)}
.backdrop{position:absolute;left:0;top:10px;width:1200px;height:560px;
  background:linear-gradient(180deg,#eef7fb 0%,#f7fbea 30%,#fbfdf6 60%,#ffffff 100%)}
.brand{position:absolute;left:216px;top:48px;width:280px;display:flex;align-items:center;gap:12px}
.brand-dot{flex:none;width:52px;height:52px;border-radius:50%;background:var(--sky)}
.brand-name{font-family:"Open Sans",sans-serif;font-weight:400;font-size:16px;color:var(--brand);line-height:1.2;white-space:nowrap}
.main-nav{position:absolute;left:562px;top:63px;width:449px;height:42px;border-radius:21px;
  background:linear-gradient(180deg,#a6def6,#6fc6ee);border:1px solid #6bbde4;display:flex;overflow:hidden}
.main-nav a{display:flex;align-items:center;justify-content:center;text-decoration:none;
  font-family:"Open Sans",sans-serif;font-weight:700;font-size:15px;color:#fff;border-right:1px solid rgba(255,255,255,.45)}
.main-nav a:last-child{border-right:0}
.main-nav .current{background:linear-gradient(180deg,#d3e85a,#b3d12b);color:#111;width:87px;padding-left:6px}
.nav-about{width:79px}.nav-services{width:92px}.nav-blog{width:66px}.nav-contact{flex:1}
.slider-art{position:absolute;left:190px;top:168px;width:855px;height:362px;border-radius:40px;
  background:radial-gradient(ellipse at 50% 50%,#ffffff 0%,#ececec 55%,rgba(230,240,245,.3) 100%)}
.slide-arrow{position:absolute;top:340px}
.slide-arrow.prev{left:148px}.slide-arrow.next{left:1058px}
.slide-caption{position:absolute;left:358px;top:515px;width:382px;height:53px;background:#fff;
  border-top:1px solid #e6e6e6;border-bottom:1px dotted #cfcfcf;
  font-family:"Encode Sans Condensed",sans-serif;font-weight:400;font-size:29px;color:#1a1a1a;
  text-align:center;line-height:50px}
.slide-dots{position:absolute;left:942px;top:553px;display:flex;gap:6px}
.slide-dots span{width:13px;height:12px;border-radius:50%;background:#9a9a9a}
.slide-dots .active{background:var(--sky-deep)}
.col{position:absolute;width:227px}
.col h2{font-family:"Encode Sans Condensed",sans-serif;font-weight:600;font-size:20px;color:var(--ink-soft);letter-spacing:-.5px;line-height:26px;white-space:nowrap}
.col p{margin-top:8px;font-size:12.2px;line-height:15.6px;letter-spacing:.5px;text-align:justify;hyphens:auto;-webkit-hyphens:auto;color:var(--ink)}
.read-more{display:flex;align-items:center;gap:5px;margin-top:11px;font-weight:700;font-size:12px;color:#222;text-decoration:none}
.read-more i{width:22px;height:14px;border-radius:7px;background:var(--sky)}
.attribution{text-align:right;font-weight:700;font-size:12px;line-height:14.5px;letter-spacing:.3px;margin-top:3px}
.divider{position:absolute;width:1px;background:var(--rule)}
.footer-line{position:absolute;left:0;top:985px;width:1200px;height:6px;background:var(--lime-soft)}
.site-footer{position:absolute;left:0;top:991px;width:1200px;height:61px;background:var(--footer-sky)}
.footer-brand{position:absolute;left:210px;top:12px;display:flex;align-items:center;gap:8px}
.footer-brand i{width:24px;height:24px;border-radius:50%;background:#9a9a9a}
.footer-brand span{font-family:"Open Sans",sans-serif;font-size:13px;color:#6b6b6b}
.footer-nav{position:absolute;left:424px;top:12px;font-family:"Open Sans",sans-serif;font-size:13px;color:#111}
.footer-nav a{color:#111;text-decoration:none}
.footer-nav .sep{margin:0 14px}
.copyright{position:absolute;left:0;width:1212px;top:42px;text-align:center;font-family:Arial,sans-serif;font-size:11px;color:#111}
.social{position:absolute;left:942px;top:6px;display:flex;gap:4px}
.social span{width:32px;height:32px;border-radius:50%}
.social .one{background:#4fb1e6}.social .two{background:var(--lime)}
</style>
</head>
<body>
<div class="top-band"></div>
<div class="backdrop"></div>

<header>
  <div class="brand"><span class="brand-dot"></span><span class="brand-name">Workforce Messaging Group</span></div>
  <nav class="main-nav">
    <a class="current" href="#">HOME</a>
    <a class="nav-about" href="#">ABOUT</a>
    <a class="nav-services" href="#">SERVICES</a>
    <a class="nav-blog" href="#">BLOG</a>
    <a class="nav-contact" href="#">CONTACT US</a>
  </nav>
</header>

<section class="slider">
  <div class="slider-art" role="img" aria-label="Illustration of three white figures in circles: one on a phone, one with a headset and laptop, one cheering, joined by curved arrows"></div>
  <svg class="slide-arrow prev" width="38" height="42" viewBox="0 0 38 42"><path d="M36 0 L14 21 L36 42 L20 42 L0 21 L20 0 Z" fill="#b5d02c"/></svg>
  <svg class="slide-arrow next" width="38" height="42" viewBox="0 0 38 42"><path d="M2 0 L24 21 L2 42 L18 42 L38 21 L18 0 Z" fill="#b5d02c"/></svg>
  <div class="slide-caption">Effective Communication</div>
  <div class="slide-dots"><span class="active"></span><span></span><span></span><span></span></div>
</section>

<main>
  <article class="col" style="left:209px;top:605px">
    <h2>External Communication</h2>
    <p>Effective communication in the workplace is the backbone of any business. Without it, you could miss out on important opportunities, waste time and cause your employees and customers to become frustrated.</p>
    <a class="read-more" href="#"><i></i>Read More</a>
  </article>
  <article class="col" style="left:488px;top:605px">
    <h2>Business Growth</h2>
    <p>Effective communication in the workplace is the backbone of any business. Without it, you could miss out on important opportunities, waste time and cause your employees and customers to become frustrated.</p>
    <a class="read-more" href="#"><i></i>Read More</a>
  </article>
  <article class="col" style="left:764px;top:605px">
    <h2>Internal Communication</h2>
    <p>Effective communication in the workplace is the backbone of any business. Without it, you could miss out on important opportunities, waste time and cause your employees and customers to become frustrated.</p>
    <a class="read-more" href="#"><i></i>Read More</a>
  </article>

  <article class="col" style="left:209px;top:801px">
    <h2>What Customers are Saying...</h2>
    <p>WMG is a great benchmarking tool."The WMG channels offer a very effective way to communicate with geographically distributed stores and in a retail environment."</p>
    <div class="attribution">Marlene Ostrander<br>Internal Communications<br>Manager</div>
  </article>
  <article class="col" style="left:488px;top:801px">
    <h2>Internal Social Media</h2>
    <p>WMG is a great benchmarking tool."The WMG channels offer a very effective way to communicate with geographically distributed stores and in a retail environment."</p>
    <div class="attribution">Specifically for employee<br>communication</div>
  </article>
  <article class="col" style="left:765px;top:801px">
    <h2>Business Growth</h2>
    <p>WMG is a great benchmarking tool."The WMG channels offer a very effective way to communicate with geographically distributed stores and in a retail environment."</p>
    <div class="attribution">Specifically for employee<br>communication</div>
  </article>

  <div class="divider" style="left:461px;top:628px;height:135px"></div>
  <div class="divider" style="left:737px;top:628px;height:135px"></div>
  <div class="divider" style="left:461px;top:830px;height:110px"></div>
  <div class="divider" style="left:740px;top:830px;height:110px"></div>
</main>

<div class="footer-line"></div>
<footer class="site-footer">
  <div class="footer-brand"><i></i><span>WMG</span></div>
  <nav class="footer-nav"><a href="#">Home</a><span class="sep">|</span><a href="#">About</a><span class="sep">|</span><a href="#">Services</a><span class="sep">|</span><a href="#">Blog</a><span class="sep">|</span><a href="#">Contact Us</a></nav>
  <div class="copyright">All rights reserved. © Workforce Messaging Group 2008</div>
  <div class="social"><span class="one"></span><span class="two"></span></div>
</footer>
</body>
</html>
```